Silver Harbor Dental Clinic Flyer

I need to make a flyer Design for my clinic (Silver Harbor Dental Clinic) Based in Philippines, Makati .
We are Providing dental Service for high end market in the Philippines. Our speciality is Dental Aesthetic/Beautification. Our targets are actors/actresses, athletes, middle to high end
We are going to place this flyers in places like Ridgeway Fitness . and other lifestyle related places

Target Market(s)

Mid to high market

Industry/Entity Type

Dental Clinic

Font styles to use
Serif

Requirements
Must have
• The flyer should Contain Our address and the services that we offer
• #4821 Orchid Tower Makati Dalisay Cor. Verano St. Lumen Square .Makati
• Email: info@silverharbor.example.ph
• mobile +639051274806
• Landline:(02)5162947
• instagram:@shdc.ph
• facebook:SHDC.ph
• Our Services :
• General Dentistry ,Orthodontics ,Cosmetic Dentistry ,Pediatric Dentistry ,Teeth Whitening,Dental Implants ,Wisdom Tooth Extraction,Root Canal Therapy
• Silver Harbor Kids Treatment:
• Teeth Cleaning , Flouride Application ,Tooth Colored Filing ,Extraction ,Pit and Fissure Sealants, Space Management
Nice to have
• Nice to have a nice tagline

```html
<!DOCTYPE html>
<html lang="en">
<head>
<meta charset="utf-8">
<title>Silver Harbor Dental Clinic Flyer</title>
<link rel="stylesheet" href="https://fonts.googleapis.com/css2?family=Cinzel:wght@400;500&family=Cormorant+Garamond:wght@500;600&family=Lora:wght@400;500&display=swap">
<style>
  :root {
    --ink: #141414;
    --paper: #f4f4f4;
    --band: #0c0c0c;
    --silver: #c9c9c9;
    --steel: #7d8a88;
    --muted: #3a3a3a;
    --white: #ffffff;
    --backdrop: #e6e6e6;
  }
  html, body {
    margin: 0;
    width: 1021px;
    height: 1200px;
    overflow: hidden;
    background: var(--backdrop);
  }
  .flyer {
    position: absolute;
    left: 60px;
    top: 17px;
    width: 850px;
    height: 1100px;
    transform: scale(1.06);
    transform-origin: 0 0;
    background: linear-gradient(180deg, #ffffff 0%, var(--paper) 40%, #ececec 100%);
    overflow: hidden;
    box-shadow: 0 2px 10px rgba(0,0,0,.18);
    color: var(--ink);
  }
  .hero-photo {
    position: absolute;
    left: 474px; top: 0;
    width: 376px; height: 430px;
    background: radial-gradient(ellipse at 55% 40%, #f1d3bf 0%, #e3bca3 35%, #d8d8d8 75%, #ececec 100%);
  }
  .bands { position: absolute; inset: 0; }
  .headline {
    position: absolute;
    left: 44px; top: 72px;
    margin: 0;
    font-family: "Cinzel", serif;
    font-weight: 400;
    font-size: 38px;
    line-height: 56px;
    letter-spacing: 1px;
  }
  .now-open {
    position: absolute;
    left: 46px; top: 190px;
    width: 334px;
    display: flex; align-items: center; gap: 10px;
    font-family: "Cinzel", serif;
    font-size: 24px;
    letter-spacing: 1px;
  }
  .now-open::before, .now-open::after {
    content: ""; flex: 1; height: 1.5px; background: var(--ink);
  }
  .clinic-name {
    position: absolute;
    left: 50px; top: 420px;
    width: 330px;
    text-align: center;
    font-family: "Cinzel", serif;
    font-weight: 500;
    color: var(--steel);
    font-size: 27px;
    line-height: 36px;
    letter-spacing: 2px;
    margin: 0;
  }
  .photo-circle {
    position: absolute;
    width: 232px; height: 232px;
    border-radius: 50%;
    border: 12px solid var(--silver);
    box-sizing: border-box;
  }
  .photo-circle.treatment-room { left: 586px; top: 351px; background: linear-gradient(160deg, #e8e8e8, #9a9a9a 55%, #3c3c3c); }
  .photo-circle.reception { left: 586px; top: 546px; background: linear-gradient(180deg, #bdbdbd, #f2f2f2 55%, #d0d0d0); }
  .photo-circle.dental-chair { left: 586px; top: 746px; background: linear-gradient(200deg, #d9cfc6, #b8b8b8 50%, #7b7b7b); }
  .section-title {
    position: absolute; left: 44px; margin: 0;
    font-family: "Cinzel", serif;
    font-weight: 500; font-size: 20px; letter-spacing: .3px;
  }
  .services-title { top: 556px; }
  .kids-title { top: 742px; }
  .service-list {
    position: absolute; left: 46px;
    margin: 0; padding: 0; list-style: none;
    display: grid; grid-template-columns: 240px 260px; grid-auto-rows: 29.5px;
    font-family: "Cormorant Garamond", serif;
    font-weight: 500; font-size: 23px; color: var(--muted);
  }
  .services-list { top: 596px; }
  .kids-list { top: 782px; }
  .service-list li { display: flex; align-items: center; gap: 9px; white-space: nowrap; }
  .service-list li::before {
    content: "›"; display: inline-flex; align-items: center; justify-content: center;
    width: 13px; height: 13px; border: 1.5px solid var(--muted); border-radius: 50%;
    font-size: 13px; line-height: 1; font-weight: 600;
  }
  .social {
    position: absolute; left: 44px; top: 892px;
    display: flex; gap: 30px;
    font-family: "Lora", serif; font-size: 15px;
  }
  .social span { display: flex; align-items: center; gap: 10px; }
  .social span::before {
    content: ""; width: 36px; height: 36px; border-radius: 50%; background: var(--ink);
  }
  .contact {
    position: absolute; left: 0; width: 850px; text-align: center;
    font-family: "Lora", serif; color: var(--white); margin: 0;
  }
  .phones { top: 992px; font-size: 22px; letter-spacing: .5px; }
  .email { top: 1030px; font-size: 16px; }
  .address { top: 1060px; font-size: 16px; font-weight: 500; }
</style>
</head>
<body>
<main class="flyer">
  <div class="hero-photo" role="img" aria-label="Portrait photo of a smiling woman touching her cheek"></div>

  <svg class="bands" viewBox="0 0 850 1100" aria-hidden="true">
    <defs>
      <linearGradient id="swooshEdge" x1="0" x2="1">
        <stop offset="0" stop-color="#9a9a9a"/><stop offset="1" stop-color="#e5e5e5"/>
      </linearGradient>
      <radialGradient id="footerShade" cx=".5" cy=".2" r=".8">
        <stop offset="0" stop-color="#3a3a3a"/><stop offset=".6" stop-color="#0c0c0c"/>
      </radialGradient>
    </defs>
    <path d="M0,344 Q260,292 630,400 Q280,330 0,356 Z" fill="url(#swooshEdge)"/>
    <path d="M0,355 Q260,300 624,405 Q300,560 0,512 Z" fill="var(--band)"/>
    <path d="M0,512 Q300,560 624,405 Q330,580 0,526 Z" fill="#cfcfcf"/>
    <path d="M624,405 Q760,440 850,455 L850,520 Q740,470 624,405 Z" fill="var(--band)"/>
    <path d="M0,925 Q425,1005 850,925 L850,938 Q425,1012 0,938 Z" fill="#bdbdbd"/>
    <path d="M0,938 Q425,1012 850,938 L850,1100 L0,1100 Z" fill="url(#footerShade)"/>
  </svg>

  <h1 class="headline">TRANSFORM YOUR<br>SMILE TO WOW!</h1>
  <div class="now-open">NOW OPEN</div>

  <p class="clinic-name">SILVER HARBOR<br>DENTAL CLINIC</p>

  <div class="photo-circle treatment-room" role="img" aria-label="Photo of a clinic treatment room with dental chairs"></div>
  <div class="photo-circle reception" role="img" aria-label="Photo of the clinic reception area"></div>
  <div class="photo-circle dental-chair" role="img" aria-label="Photo of a dental chair in a treatment room"></div>

  <h2 class="section-title services-title">OUR SERVICES</h2>
  <ul class="service-list services-list">
    <li>General Dentistry</li><li>Teeth Whitening</li>
    <li>Orthodontics</li><li>Dental Implants</li>
    <li>Cosmetic Dentistry</li><li>Wisdom Tooth Extraction</li>
    <li>Pediatric Dentistry</li><li>Root Canal Therapy</li>
  </ul>

  <h2 class="section-title kids-title">SILVER HARBOR KIDS TREATMENT</h2>
  <ul class="service-list kids-list">
    <li>Teeth Cleaning</li><li>Extraction</li>
    <li>Flouride Application</li><li>Pit and Fissure Sealants</li>
    <li>Tooth Colored Filing</li><li>Space Management</li>
  </ul>

  <div class="social"><span>SHDC.ph</span><span>@shdc.ph</span></div>

  <p class="contact phones">+639051274806 &nbsp;|&nbsp; (02)5162947</p>
  <p class="contact email">info@silverharbor.example.ph</p>
  <p class="contact address">#4821 Orchid Tower Makati Dalisay Cor. Verano St. Lumen Square .Makati</p>
</main>
</body>
</html>
```